Retail Jewelry Business Card Design Project

We are in need of a new business card design for a retail jewelry store. This store is in the business of fine jewelry including but not specific to bridal jewelry, diamonds, designer jewelry and watches.

This store has been in business for 20 years but continues to strive for a modern professional appeal. The main colors use for this business are a royal blue, white and silver.

Target Market(s)

Target market is ages 18-50

Industry/Entity Type

Jewelry

Requirements
Must have
• Sales Person Name
Sales Person Email Address

Store Address
Store Phone
Website

Standard business card size. No odd shapes or sizes.
Nice to have
• Overall modern feel for card.

We have thought that a design with a nice feature of the logo on the back of the card would be nice but open to ideas.
Should not have
• No specific images of jewelry should be used.

```html
<!DOCTYPE html>
<html lang="en">
<head>
<meta charset="utf-8">
<title>Harlan Reed Fine Jewelry – Business Card</title>
<link rel="stylesheet" href="https://fonts.googleapis.com/css2?family=Crimson+Text:wght@400;600;700&family=Great+Vibes&display=swap">
<style>
  :root {
    --royal: #2a2fc4;
    --royal-deep: #0b0a4a;
    --silver: #c9ccd3;
    --silver-dark: #8c9099;
    --paper: #eceef1;
    --ink: #3a3a40;
    --backdrop: #c4c4c4;
    --white: #ffffff;
  }
  * { margin: 0; padding: 0; box-sizing: border-box; }
  html, body { width: 1200px; height: 861px; overflow: hidden; }
  body {
    background: var(--backdrop);
    font-family: "Crimson Text", Georgia, serif;
    color: var(--ink);
    position: relative;
  }
  .card {
    position: absolute;
    top: 140px;
    width: 340px;
    height: 580px;
    background: var(--paper);
    box-shadow: 0 10px 24px rgba(0,0,0,.25);
    overflow: hidden;
  }
  .card--services { left: 210px; }
  .card--contact { left: 650px; }
  .card-art { position: absolute; inset: 0; }
  .brand {
    position: absolute;
    top: 60px; left: 40px; right: 40px;
    text-align: center;
    color: var(--white);
    font-family: "Crimson Text", Georgia, serif;
    font-weight: 400;
    font-size: 30px;
    line-height: 1.15;
  }
  .content { position: absolute; left: 34px; right: 30px; top: 255px; }
  .script-title {
    font-family: "Great Vibes", cursive;
    color: var(--royal);
    font-weight: 400;
    line-height: 1;
  }
  .services-title { text-align: center; margin-bottom: 12px; font-size: 44px; }
  .services-intro { font-weight: 700; font-size: 15px; line-height: 1.2; margin-bottom: 8px; }
  .services-list { list-style: none; font-size: 15px; line-height: 1.3; }
  .services-list li { padding-left: 14px; position: relative; }
  .services-list li::before {
    content: ""; position: absolute; left: 0; top: 8px;
    width: 5px; height: 5px; border-radius: 50%; background: var(--royal);
  }
  .person-name { margin-bottom: 18px; font-size: 46px; }
  .contact-list { list-style: none; font-size: 15px; line-height: 1.35; }
  .contact-list li { display: flex; align-items: flex-start; gap: 9px; }
  .contact-icon { flex: 0 0 16px; width: 16px; height: 16px; margin-top: 2px; }
  .contact-spacer { flex: 0 0 16px; }
</style>
</head>
<body>

<section class="card card--services">
  <svg class="card-art" viewBox="0 0 340 580">
    <defs>
      <linearGradient id="bandServices" x1="1" y1="0" x2="0.2" y2="1">
        <stop offset="0" stop-color="#2a2fc4"/>
        <stop offset="1" stop-color="#0b0a4a"/>
      </linearGradient>
    </defs>
    <rect width="340" height="580" fill="#eceef1" role="img" aria-label="Light silver damask pattern background"/>
    <path d="M0 0 H340 V225 Q170 140 0 225 Z" fill="url(#bandServices)"/>
    <path d="M0 225 Q170 140 340 225" fill="none" stroke="#c9ccd3" stroke-width="4"/>
    <ellipse cx="170" cy="178" rx="60" ry="22" fill="#8c9099" opacity=".8" role="img" aria-label="Silver filigree flourish ornament"/>
  </svg>
  <div class="brand">Harlan Reed Fine Jewelry</div>
  <div class="content">
    <h2 class="script-title services-title">Our Services</h2>
    <p class="services-intro">We offer a full compliment of jewelry and watch services, including:</p>
    <ul class="services-list">
      <li>Ring Sizing</li>
      <li>Ring Shank Replacement</li>
      <li>Soldering</li>
      <li>Laser Welding</li>
      <li>Stone Tightening</li>
      <li>Ring Retipping/Head Replacement</li>
      <li>Ring Refinishing</li>
      <li>Pearl Restringing</li>
      <li>Engraving</li>
      <li>Sell Us Your Gold, Silver and Coins</li>
    </ul>
  </div>
</section>

<section class="card card--contact">
  <svg class="card-art" viewBox="0 0 340 580">
    <defs>
      <linearGradient id="bandContact" x1="1" y1="0" x2="0.2" y2="1">
        <stop offset="0" stop-color="#2a2fc4"/>
        <stop offset="1" stop-color="#0b0a4a"/>
      </linearGradient>
    </defs>
    <rect width="340" height="580" fill="#eceef1" role="img" aria-label="Light silver damask pattern background"/>
    <path d="M0 0 H340 V225 Q170 140 0 225 Z" fill="url(#bandContact)"/>
    <path d="M0 225 Q170 140 340 225" fill="none" stroke="#c9ccd3" stroke-width="4"/>
    <ellipse cx="170" cy="178" rx="60" ry="22" fill="#8c9099" opacity=".8" role="img" aria-label="Silver filigree flourish ornament"/>
  </svg>
  <div class="brand">Harlan Reed Fine Jewelry</div>
  <div class="content">
    <h1 class="script-title person-name">Harlan Reed<br>Whitcombe</h1>
    <ul class="contact-list">
      <li>
        <svg class="contact-icon" viewBox="0 0 16 16" aria-label="Address"><circle cx="8" cy="8" r="8" fill="#2a2fc4"/><path d="M8 3.5a3 3 0 0 0-3 3c0 2.2 3 5.5 3 5.5s3-3.3 3-5.5a3 3 0 0 0-3-3z" fill="#fff"/><circle cx="8" cy="6.5" r="1.1" fill="#2a2fc4"/></svg>
        <span>2280 Marlow Avenue<br>Bayport City, FL 30000</span>
      </li>
      <li>
        <svg class="contact-icon" viewBox="0 0 16 16" aria-label="Phone"><circle cx="8" cy="8" r="8" fill="#2a2fc4"/><path d="M5.2 4h1.6l.7 2-1 .8a5 5 0 0 0 2.7 2.7l.8-1 2 .7v1.6c0 .5-.4.8-.9.8A7 7 0 0 1 4.4 4.9c0-.5.3-.9.8-.9z" fill="#fff"/></svg>
        <span>(555) 014-2291</span>
      </li>
      <li>
        <svg class="contact-icon" viewBox="0 0 16 16" aria-label="Email"><circle cx="8" cy="8" r="8" fill="#2a2fc4"/><rect x="4" y="5.2" width="8" height="5.6" fill="#fff"/><path d="M4 5.2 8 8.4 12 5.2" fill="none" stroke="#2a2fc4" stroke-width=".9"/></svg>
        <span>harlan@harlanreedjewelry.com</span>
      </li>
      <li>
        <svg class="contact-icon" viewBox="0 0 16 16" aria-label="Website"><circle cx="8" cy="8" r="8" fill="#2a2fc4"/><circle cx="8" cy="8" r="4" fill="none" stroke="#fff" stroke-width="1"/><path d="M4 8h8M8 4c-1.6 2.4-1.6 5.6 0 8M8 4c1.6 2.4 1.6 5.6 0 8" fill="none" stroke="#fff" stroke-width=".8"/></svg>
        <span>www.harlanreedjewelry.com</span>
      </li>
      <li>
        <svg class="contact-icon" viewBox="0 0 16 16" aria-label="Social page"><circle cx="8" cy="8" r="8" fill="#2a2fc4"/></svg>
        <span>HarlanReedFineJewelry</span>
      </li>
      <li>
        <span class="contact-spacer"></span>
        <span>harlanreedyes</span>
      </li>
    </ul>
  </div>
</section>

</body>
</html>
```